Create Template Proposal Coversheet

We need a proposal Cover Sheet & Page Template for residential architectural projects. For the Cover Sheet, we want a variety of images blends and set as a background image for the title of the proposal for prospective clients. We need it in a format that we can type over the top of the image (maybe whited-out in the middle) so we can use it for all our proposals. Our logo should be clear and sharp in a corner (but we will leave that up to the designer. Not all images need to be used. For the Page Template we want a consistent look on the page with our logo, company address & contact information and a design element that ties the entire proposal together. Our proposals consist of a Cover page, Project information sheet, a picture of the property, the proposal for services (3-5 pages), Expect fees page and a timeline page.

Target Market(s)

Homeowners, 35 - 60 years old

Industry/Entity Type

Architecture

Font styles to use
Serif

Colors
3176b5
f68d4c
ec1f27
fbee3f

Requirements
Must have
• The cover should have a nice blend of images - looking for something that shows the whole design process - from initial sketches to working drawings, construction and finished home. These images are background to the title of the proposal

```html
<!DOCTYPE html>
<html lang="en">
<head>
<meta charset="utf-8">
<title>Architect Proposal Template</title>
<link href="https://fonts.googleapis.com/css2?family=Cinzel:wght@400;500;700&family=Tinos:ital,wght@0,400;0,700;1,400&family=Source+Sans+3:ital@1&display=swap" rel="stylesheet">
<style>
:root{
  --navy:#2b2a72;
  --orange:#f37c21;
  --peach:#f3c29a;
  --red:#e0262b;
  --yellow:#f4ec3a;
  --blue:#2e3c9c;
  --ink:#2a2a2a;
  --grey:#8a8a8a;
  --canvas:#ebebeb;
  --white:#ffffff;
  --head:'Cinzel',serif;
  --body:'Tinos',serif;
  --sans:'Source Sans 3',sans-serif;
}
*{margin:0;padding:0;box-sizing:border-box}
html,body{width:1200px;height:1012px;overflow:hidden;background:var(--canvas)}
.sheet{position:relative;width:1200px;height:1012px}
.page{position:absolute;width:361px;height:468px;background:var(--white);overflow:hidden;font-family:var(--body);color:var(--ink)}
.p1{left:39px;top:30px}.p2{left:419px;top:30px}.p3{left:799px;top:30px}
.p4{left:39px;top:515px}.p5{left:419px;top:515px}.p6{left:799px;top:515px}
.abs{position:absolute}
.band{position:absolute;left:0;width:361px;height:10px;z-index:2}
.band.top{top:0}.band.bottom{bottom:0}
.cover-blend{position:absolute;left:0;top:0;width:361px;height:468px;
  background:
    linear-gradient(180deg,rgba(255,255,255,0) 55%,rgba(255,255,255,.92) 86%),
    linear-gradient(155deg,#e4e6ea 0%,#c7d6ec 28%,#d9b08a 55%,#a9bd8f 80%,#dfe6d6 100%);
  opacity:.55}
.cover-shape{position:absolute;left:0;top:0}
.tagline{position:absolute;left:24px;top:14px;font-family:var(--head);font-weight:400;font-size:13px;color:var(--white);letter-spacing:.3px}
.cover-title{position:absolute;left:25px;top:68px;font-family:var(--head);font-weight:700;font-size:28px;line-height:30px;color:var(--white)}
.cover-rule{position:absolute;left:27px;top:142px;width:56px;height:2px;background:var(--white)}
.cover-address{position:absolute;left:27px;top:160px;font-family:var(--sans);font-style:italic;font-size:6.4px;line-height:8.5px;color:var(--white)}
.cover-year{position:absolute;left:27px;top:203px;font-family:var(--sans);font-style:italic;font-size:6.4px;color:var(--white)}
.brand{position:absolute;right:18px;bottom:22px;display:flex;align-items:center;gap:6px;font-family:var(--head);font-weight:700;color:var(--navy);text-align:center}
.brand .mark{width:10px;height:10px;background:var(--navy)}
.brand .name{font-size:14px;line-height:14px}
.brand .sub{font-size:6px;letter-spacing:3px;line-height:8px}
.panel-title{position:absolute;font-family:var(--head);font-weight:400;font-size:13.5px;line-height:17.5px;color:var(--white)}
.item{position:absolute;width:100px;text-align:center;font-size:4.6px;line-height:5.6px;color:var(--ink)}
.item b{display:block;font-weight:400;font-size:6px;line-height:7px;letter-spacing:.2px}
.photo{position:absolute}
.h2{position:absolute;font-family:var(--head);font-weight:400;font-size:12.5px;color:var(--navy)}
.small-caps{position:absolute;font-size:5.6px;letter-spacing:.3px;font-weight:700;color:var(--ink)}
.lbl{position:absolute;font-size:5.6px;line-height:6.5px;text-align:center;color:var(--ink);transform:translateX(-50%);white-space:nowrap}
.bar{position:absolute;height:12px;color:var(--white);font-family:var(--sans);font-size:5px;letter-spacing:2.5px;display:flex;align-items:center;justify-content:center;font-style:normal}
.price-table{position:absolute;left:8px;top:46px;border-collapse:collapse;font-size:5.6px;color:var(--ink)}
.price-table td,.price-table th{text-align:center;padding:0}
.price-table .hd th{background:var(--orange);color:var(--white);font-family:var(--sans);font-style:normal;font-weight:400;font-size:5px;letter-spacing:.6px;height:10px;border:1px solid var(--navy);border-bottom:none}
.price-table .sub td{height:12px;border-left:1px solid var(--navy);border-right:1px solid var(--navy)}
.price-table .row td.cell{height:23px;border:1px solid var(--navy)}
.price-table .lab{text-align:right;padding-right:4px;width:52px}
.split{display:flex;justify-content:space-around}
.para{position:absolute;font-size:6.6px;line-height:8.9px;text-align:justify;color:var(--ink)}
.para em{font-style:normal;color:var(--navy)}
.prices{position:absolute;left:14px;top:170px;font-size:7.4px;line-height:10px;color:var(--navy)}
.prices div{display:flex;width:112px;justify-content:space-between}
.total{position:absolute;left:14px;top:230px;font-size:7.4px;line-height:10px;width:112px}
.total .t{display:flex;justify-content:space-between;color:var(--orange)}
.footer{position:absolute;left:0;bottom:0;width:361px;height:43px;background:var(--navy);color:var(--white);font-size:5.3px;line-height:7.5px;text-align:center}
.footer div{position:absolute;top:12px}
</style>
</head>
<body>
<div class="sheet">

  <!-- Cover, navy edition -->
  <section class="page p1">
    <div class="cover-blend" role="img" aria-label="Blended background of initial sketches, working drawings, construction and finished home"></div>
    <div class="band top" style="background:var(--navy)"></div>
    <svg class="cover-shape" width="361" height="468" aria-hidden="true"><polygon points="14,0 226,0 226,224 14,338" fill="var(--navy)" fill-opacity=".94"/></svg>
    <div class="tagline">A Home Like NO Other</div>
    <h1 class="cover-title">ARCHITECT<br>PROPOSAL</h1>
    <div class="cover-rule"></div>
    <p class="cover-address">Lorem ipsum dolor sit amet,<br>12/ 2345, Address,<br>Street, Road , NY,<br>USA.</p>
    <p class="cover-year">2020</p>
    <div class="brand"><span class="mark"></span><div><div class="name">HARLAN REEVE</div><div class="sub">ARCHITECT</div></div></div>
    <div class="band bottom" style="background:var(--navy)"></div>
  </section>

  <!-- Cover, orange edition -->
  <section class="page p2">
    <div class="cover-blend" role="img" aria-label="Blended background of initial sketches, working drawings, construction and finished home"></div>
    <div class="band top" style="background:var(--orange)"></div>
    <svg class="cover-shape" width="361" height="468" aria-hidden="true"><polygon points="14,0 226,0 226,224 14,338" fill="var(--orange)" fill-opacity=".94"/></svg>
    <div class="tagline">A Home Like NO Other</div>
    <h1 class="cover-title">ARCHITECT<br>PROPOSAL</h1>
    <div class="cover-rule"></div>
    <p class="cover-address" style="top:164px">Lorem ipsum dolor sit amet,<br>12/ 2345, Address,<br>Street, Road , NY,<br>USA.</p>
    <p class="cover-year" style="top:207px">2020</p>
    <div class="brand"><span class="mark"></span><div><div class="name">HARLAN REEVE</div><div class="sub">ARCHITECT</div></div></div>
    <div class="band bottom" style="background:var(--orange)"></div>
  </section>

  <!-- Services, navy -->
  <section class="page p3">
    <div class="abs" style="left:0;top:0;width:127px;height:231px;background:var(--navy)"></div>
    <div class="photo" role="img" aria-label="Rolled architectural blueprints" style="left:0;top:231px;width:127px;height:237px;background:linear-gradient(135deg,#c9d8ef,#f2f6fc 45%,#8fb0dc)"></div>
    <svg class="abs" style="left:0;top:0" width="127" height="231" aria-hidden="true"><path d="M0,118 A125,125 0 0 1 92,231" fill="none" stroke="var(--white)" stroke-width="3"/></svg>
    <h2 class="panel-title" style="right:251px;top:15px;text-align:right;width:110px">Lorem Ipsum<br>Dolor Sit<br>Services</h2>
    <svg class="abs" style="left:0;top:0" width="361" height="468" aria-hidden="true" fill="none" stroke="var(--navy)" stroke-width="1.2">
      <line x1="297" y1="18" x2="297" y2="448"/>
      <g fill="var(--white)">
        <circle cx="297" cy="34" r="7"/><circle cx="297" cy="91" r="7"/><circle cx="297" cy="148" r="7"/><circle cx="297" cy="205" r="7"/>
        <circle cx="297" cy="262" r="7"/><circle cx="297" cy="319" r="7"/><circle cx="297" cy="376" r="7"/><circle cx="297" cy="433" r="7"/>
      </g>
      <line x1="268" y1="35" x2="290" y2="35"/><line x1="237" y1="92" x2="290" y2="92"/>
      <line x1="268" y1="149" x2="290" y2="149"/><line x1="237" y1="206" x2="290" y2="206"/>
      <line x1="268" y1="263" x2="290" y2="263"/><line x1="237" y1="320" x2="290" y2="320"/>
      <line x1="268" y1="377" x2="290" y2="377"/><line x1="237" y1="434" x2="290" y2="434"/>
      <g stroke-width="1.5">
        <path d="M334,22 L324,46 M334,22 L344,46 M327,38 L341,38"/><circle cx="334" cy="24" r="2.5"/>
        <rect x="322" y="79" width="24" height="24"/><path d="M328,85 H340 M334,85 V98"/>
        <path d="M322,136 V160 H346 M327,160 V142 M332,160 V147 M322,150 L338,160"/>
        <path d="M326,193 V213 H346 M322,197 H342 V217 M326,213 L342,197"/>
        <circle cx="334" cy="256" r="7"/><path d="M334,263 V273 M334,268 Q326,268 324,262 M334,268 Q342,268 344,262"/>
        <rect x="322" y="307" width="24" height="24" rx="1"/><path d="M334,307 V331 M322,319 H346"/>
        <circle cx="334" cy="366" r="3"/><circle cx="326" cy="380" r="3"/><circle cx="342" cy="380" r="3"/><path d="M322,388 H346 M334,369 V375 L326,377 M334,375 L342,377"/>
        <circle cx="334" cy="433" r="11"/><circle cx="334" cy="433" r="5"/><path d="M334,418 V425 M334,441 V448 M319,433 H326 M342,433 H349"/>
      </g>
    </svg>
    <div class="item" style="left:168px;top:23px"><b>LOREM IPSUM</b>Lorem ipsum dolor sit amet, consec-<br>tetuer adipiscing elit,</div>
    <div class="item" style="left:137px;top:80px"><b>LOREM IPSUM</b>Lorem ipsum dolor sit amet, consec-<br>tetuer adipiscing elit,</div>
    <div class="item" style="left:168px;top:137px"><b>LOREM IPSUM</b>Lorem ipsum dolor sit amet, consec-<br>tetuer adipiscing elit,</div>
    <div class="item" style="left:137px;top:194px"><b>LOREM IPSUM</b>Lorem ipsum dolor sit amet, consec-<br>tetuer adipiscing elit,</div>
    <div class="item" style="left:168px;top:251px"><b>LOREM IPSUM</b>Lorem ipsum dolor sit amet, consec-<br>tetuer adipiscing elit,</div>
    <div class="item" style="left:137px;top:308px"><b>LOREM IPSUM</b>Lorem ipsum dolor sit amet, consec-<br>tetuer adipiscing elit,</div>
    <div class="item" style="left:168px;top:365px"><b>LOREM IPSUM</b>Lorem ipsum dolor sit amet, consec-<br>tetuer adipiscing elit,</div>
    <div class="item" style="left:137px;top:422px"><b>LOREM IPSUM</b>Lorem ipsum dolor sit amet, consec-<br>tetuer adipiscing elit,</div>
  </section>

  <!-- Services, orange -->
  <section class="page p4">
    <div class="abs" style="left:237px;top:0;width:124px;height:228px;background:var(--orange)"></div>
    <div class="photo" role="img" aria-label="Rolled architectural drawings in warm peach tone" style="left:237px;top:228px;width:124px;height:240px;background:linear-gradient(150deg,#f7d3b4,#efb68a 55%,#e9a574)"></div>
    <svg class="abs" style="left:237px;top:0" width="124" height="228" aria-hidden="true"><path d="M124,114 A115,115 0 0 0 36,228" fill="none" stroke="var(--white)" stroke-width="3"/></svg>
    <h2 class="panel-title" style="left:253px;top:11px">Lorem Ipsum<br>&nbsp;Dolor Sit<br>Services</h2>
    <svg class="abs" style="left:0;top:0" width="237" height="468" aria-hidden="true" fill="none" stroke="var(--orange)" stroke-width="1.2">
      <line x1="67" y1="16" x2="67" y2="448"/>
      <g fill="var(--white)">
        <circle cx="67" cy="32" r="7"/><circle cx="67" cy="89" r="7"/><circle cx="67" cy="146" r="7"/><circle cx="67" cy="203" r="7"/>
        <circle cx="67" cy="260" r="7"/><circle cx="67" cy="317" r="7"/><circle cx="67" cy="374" r="7"/><circle cx="67" cy="431" r="7"/>
      </g>
      <line x1="74" y1="33" x2="97" y2="33"/><line x1="74" y1="90" x2="128" y2="90"/>
      <line x1="74" y1="147" x2="97" y2="147"/><line x1="74" y1="204" x2="128" y2="204"/>
      <line x1="74" y1="261" x2="97" y2="261"/><line x1="74" y1="318" x2="128" y2="318"/>
      <line x1="74" y1="375" x2="97" y2="375"/><line x1="74" y1="432" x2="128" y2="432"/>
      <g stroke-width="1.6">
        <path d="M31,21 L45,28 L31,35 L17,28 Z M17,33 L31,40 L45,33 M17,38 L31,45 L45,38"/>
        <rect x="18" y="77" width="26" height="24"/><circle cx="31" cy="89" r="4"/>
        <path d="M22,144 A8,8 0 0 1 38,144 Z M30,144 V158 M22,158 H40 V161 H22 Z"/>
        <rect x="18" y="192" width="26" height="24" rx="1"/><rect x="23" y="198" width="16" height="13"/>
        <path d="M31,247 L43,254 V266 L31,273 L19,266 V254 Z M31,254 L37,258 V264 L31,268 L25,264 V258 Z"/>
        <rect x="18" y="306" width="26" height="18" rx="2"/><circle cx="31" cy="324" r="4"/><path d="M28,328 V334 L31,332 L34,334 V328"/>
        <circle cx="31" cy="374" r="13"/><circle cx="31" cy="374" r="8"/><circle cx="31" cy="374" r="3"/><path d="M31,374 L43,362"/>
        <path d="M26,440 C14,428 16,418 26,418 C36,418 38,428 26,440 Z"/><circle cx="36" cy="434" r="7"/><path d="M36,430 V438"/>
      </g>
    </svg>
    <div class="item" style="left:97px;top:21px"><b>LOREM IPSUM</b>Lorem ipsum dolor sit amet, consec-<br>tetuer adipiscing elit,</div>
    <div class="item" style="left:128px;top:78px"><b>LOREM IPSUM</b>Lorem ipsum dolor sit amet, consec-<br>tetuer adipiscing elit,</div>
    <div class="item" style="left:97px;top:135px"><b>LOREM IPSUM</b>Lorem ipsum dolor sit amet, consec-<br>tetuer adipiscing elit,</div>
    <div class="item" style="left:128px;top:192px"><b>LOREM IPSUM</b>Lorem ipsum dolor sit amet, consec-<br>tetuer adipiscing elit,</div>
    <div class="item" style="left:97px;top:249px"><b>LOREM IPSUM</b>Lorem ipsum dolor sit amet, consec-<br>tetuer adipiscing elit,</div>
    <div class="item" style="left:128px;top:306px"><b>LOREM IPSUM</b>Lorem ipsum dolor sit amet, consec-<br>tetuer adipiscing elit,</div>
    <div class="item" style="left:97px;top:363px"><b>LOREM IPSUM</b>Lorem ipsum dolor sit amet, consec-<br>tetuer adipiscing elit,</div>
    <div class="item" style="left:128px;top:420px"><b>LOREM IPSUM</b>Lorem ipsum dolor sit amet, consec-<br>tetuer adipiscing elit,</div>
  </section>

  <!-- Time frame -->
  <section class="page p5">
    <div class="abs" role="img" aria-label="Dotted decorative grid" style="left:4px;top:4px;width:60px;height:170px;background:linear-gradient(180deg,#eceef8,#f6f7fc)"></div>
    <div class="photo" role="img" aria-label="Timber-framed home entrance with stone pillars" style="left:70px;top:0;width:143px;height:192px;background:linear-gradient(180deg,#9fb2c9 0%,#a9603f 35%,#8a4a30 65%,#9a9890 100%)"></div>
    <div class="photo" role="img" aria-label="Timber-framed porch with trees and driveway" style="left:219px;top:0;width:142px;height:193px;background:linear-gradient(180deg,#a9c3dc 0%,#5f7a4a 30%,#a0583a 55%,#a7a49c 100%)"></div>
    <svg class="abs" style="left:0;top:0" width="361" height="200" aria-hidden="true" fill="none" stroke="var(--white)" stroke-width="2">
      <path d="M75,180 V5 H207"/><path d="M226,6 V185 H355"/>
    </svg>
    <h2 class="h2" style="left:20px;top:209px">Time Frame And Instalments</h2>
    <div class="small-caps" style="left:20px;top:242px">TRADITIONAL CONSTRUCTIONS</div>
    <div class="lbl" style="left:49px;top:260px">Site Analysis<br>&amp; Design</div>
    <div class="lbl" style="left:102px;top:268px">Permits</div>
    <div class="lbl" style="left:149px;top:259px">Site<br>Preparation</div>
    <div class="lbl" style="left:262px;top:268px">Construction</div>
    <div class="abs" style="left:20px;top:274px;width:60px;height:12px;background:#8c8c8c"></div>
    <div class="abs" style="left:83px;top:274px;width:39px;height:12px;background:#1e1e1e"></div>
    <div class="abs" style="left:126px;top:274px;width:46px;height:12px;background:#6b6b6b"></div>
    <div class="abs" style="left:176px;top:274px;width:165px;height:12px;background:#444"></div>

    <div class="small-caps" style="left:20px;top:314px">HARLAN REEVE ARCHITECT CONSTRUCTIONS</div>
    <div class="lbl" style="left:49px;top:332px">Site Analysis<br>&amp; Design</div>
    <div class="lbl" style="left:167px;top:339px">Manufacturing Lorem ipsum</div>
    <div class="lbl" style="left:296px;top:344px">Time Saved</div>
    <div class="bar" style="left:20px;top:348px;width:59px;background:var(--navy)">5 WEEKS</div>
    <div class="bar" style="left:82px;top:348px;width:166px;background:var(--orange)">6 MONTHS</div>
    <svg class="abs" style="left:0;top:340px" width="361" height="110" aria-hidden="true" fill="none">
      <path d="M251,14 H342 M251,8 V20 M342,8 V20" stroke="var(--red)" stroke-width="1.2"/>
      <g stroke="var(--blue)" stroke-width=".7" stroke-dasharray="2 2">
        <line x1="79" y1="20" x2="79" y2="90"/><line x1="198" y1="20" x2="198" y2="74"/>
        <line x1="223" y1="20" x2="223" y2="86"/><line x1="248" y1="20" x2="248" y2="86"/>
        <line x1="273" y1="20" x2="273" y2="60"/>
      </g>
    </svg>
    <div class="lbl" style="left:101px;top:381px">Permits</div>
    <div class="abs" style="left:82px;top:388px;width:38px;height:12px;background:var(--yellow)"></div>
    <div class="lbl" style="left:172px;top:373px">Site<br>Preparation</div>
    <div class="abs" style="left:149px;top:388px;width:46px;height:12px;background:var(--blue)"></div>
    <div class="lbl" style="left:291px;top:403px">Lorem ipsum<br>5%</div>
    <div class="lbl" style="left:183px;top:417px">Installation<br>30%</div>
    <div class="lbl" style="left:223px;top:428px">Finishes<br>30%</div>
    <div class="lbl" style="left:260px;top:428px">Hand Over<br>5%</div>
    <div class="lbl" style="left:79px;top:433px">Agreement<br>30%</div>
    <div class="lbl" style="left:28px;top:433px">Value<br>150K</div>
  </section>

  <!-- Prices -->
  <section class="page p6">
    <h2 class="h2" style="left:14px;top:12px">Prices And Lorem Ipsum</h2>
    <table class="price-table">
      <tr class="hd"><th></th><th style="width:57px">1 Bedroom</th><th style="width:62px">2 Bedrooms</th><th style="width:73px">3 Bedrooms</th><th style="width:93px">4 Bedrooms</th></tr>
      <tr class="sub"><td class="lab">Bathrooms</td><td>1</td><td><div class="split"><span>1</span><span>2</span></div></td><td><div class="split"><span>1</span><span>2</span><span>3</span></div></td><td><div class="split"><span>1</span><span>2</span><span>3</span><span>4</span></div></td></tr>
      <tr class="row"><td class="lab">1 story</td><td class="cell">Values</td><td class="cell">Values</td><td class="cell">Values</td><td class="cell">Values</td></tr>
      <tr class="row"><td class="lab">2 story</td><td class="cell">N/A</td><td class="cell">Values</td><td class="cell">Values</td><td class="cell">Values</td></tr>
    </table>
    <p class="para" style="left:13px;top:126px;width:138px">Lorem ipsum dolor sit amet, consectetuer adipiscing elit, sed diam nonummy nibh euismod tincidunt ut laoreet dolore magna aliquam erat volutpat. Ut wisi enim ad minim</p>
    <div class="prices">
      <div><span>Lorem ipsum dolor</span><span>$ 100,000.00</span></div>
      <div><span>Lorem ipsum dolor</span><span>$&nbsp;&nbsp;&nbsp;&nbsp; 1,000.00</span></div>
      <div><span>Lorem ipsum dolor</span><span>$&nbsp;&nbsp;&nbsp;&nbsp;&nbsp;&nbsp; 100.00</span></div>
      <div><span>Lorem ipsum dolor</span><span>$&nbsp;&nbsp;&nbsp;&nbsp; 5,000.00</span></div>
      <div><span>Lorem ipsum dolor</span><span>$&nbsp;&nbsp;&nbsp;&nbsp; 7,800.00</span></div>
    </div>
    <div class="total"><div class="t"><span>TOTAL</span><span>$ 113,900.00</span></div><div style="color:var(--navy)">TOTAL SAVE (0.2%)</div></div>
    <p class="para" style="left:12px;top:266px;width:127px">Lorem ipsum dolor sit amet, consectetuer adipiscing elit, sed diam nonummy nibh euismod tincidunt ut laoreet dolore magna aliquam erat volutpat. Ut wisi enim ad minim veniam, quis nostrud exerci tation ullamcorper suscipit lobortis nisl ut aliquip ex ea commodo consequat. Duis autem vel eum iriure dolor in hendrerit in vulputate velit esse molestie consequat, vel illum dolore eu feugiat nulla facilisis at vero eros et accumsan et iusto odio dignissim qui blandit praesent luptatum zzril delenit augue duis dolore te feugait nulla facilisi. Lorem ipsum dolor sit amet, cons ectetuer adipiscing elit, sed diam nonummy nibh euismod tincidunt ut laoreet dolore</p>
    <h2 class="h2" style="left:173px;top:132px">Cost Saving</h2>
    <p class="para" style="left:173px;top:152px;width:168px"><em>Lorem ipsum</em> dolor sit amet, consectetuer adipiscing elit, sed diam nonummy nibh euismod tincidunt ut laoreet dolore magna aliquam erat volutpat. Ut wisi enim ad <em>minim veniam</em>, quis nostrud exerci tation ullamcorper suscipit lobortis nisl ut aliquip ex ea commodo consequat. Duis autem vel eum iriure dolor in hendrerit in vulputate <em>velit esse</em> molestie consequat, vel illum dolore eu feugiat nulla facilisis at vero eros et accumsan et iusto odio <em>dignissim</em> qui blandit praesent luptatum zzril delenit augue duis dolore te feugait nulla facilisi. <em>Lorem ipsum</em> dolor sit amet, consectetuer adipiscing elit, sed diam nonummy nibh euismod tincidunt ut laoreet dolore magna aliquam erat volutpat. Ut wisi enim ad <em>minim veniam</em>, quis nostrud exerci tation ullamcorper suscipit lobortis nisl ut aliquip ex ea commodo consequat. Duis autem vel eum iriure dolor in hendrerit in vulputate <em>velit esse</em> molestie consequat, vel illum dolore eu feugiat</p>
    <div class="abs" style="left:153px;top:330px;width:208px;height:10px;background:var(--navy)"></div>
    <div class="abs" style="left:153px;top:330px;width:10px;height:100px;background:var(--navy)"></div>
    <div class="photo" role="img" aria-label="Finished timber home among trees at dusk" style="left:173px;top:317px;width:169px;height:99px;background:linear-gradient(180deg,#c8d4dc 0%,#4f6a3c 35%,#9a5632 60%,#6d7a4a 100%);border:2px solid var(--white)"></div>
    <footer class="footer">
      <div style="left:10px;width:80px">MY LOCATION (HQ)<br>44, LINDEN ROW, NY<br>USA</div>
      <div style="left:115px;width:131px;top:9px">GET ADVICE ON YOUR PROJECT<br>+1 555 014 2290<br>WWW.HARLANREEVE.COM</div>
      <div style="left:272px;width:82px">MY LOCATION (1)<br>17, ORCHARD LANE, CA<br>USA</div>
    </footer>
  </section>

</div>
</body>
</html>
```